Determining number of boxes of planks of flooring for a room

Need a creative design of an infographic of a room with instructions on how to measure the room and use this measurement to determine how much flooring to order.
The floor planks come in boxes and each box has 36 planks. Each box covers 5 metre squared in total.
The intent of the infographic is to help inform the customer how many boxes they need to order for their room.
The infographic should match the style of flooring being sold (image provided) and the logo for the company (image provided).
A crude sketch of instructions to measure a room and determine the number of boxes is provided in a document attached with this brief. Need improvement to the steps mentioned in this document on the infographic created.

```html
<!DOCTYPE html>
<html lang="en">
<head>
<meta charset="utf-8">
<title>Self Adhesive Vinyl Planks – Floor Packs Guide</title>
<link rel="stylesheet" href="https://fonts.googleapis.com/css2?family=Barlow:wght@400;500;600;700&family=Barlow+Semi+Condensed:wght@500;600;700&display=swap">
<style>
  :root{
    --ink:#5a5046;
    --ink-dark:#2b2621;
    --accent:#b57233;
    --rule:#c9c2b8;
    --plan:#f4f0e9;
    --wall:#d9cfbd;
    --room:#dcdcdc;
    --bg:#ffffff;
  }
  *{margin:0;padding:0;box-sizing:border-box}
  html,body{width:1200px;height:675px;overflow:hidden;background:var(--bg)}
  body{font-family:"Barlow",sans-serif;color:var(--ink-dark);position:relative}
  .abs{position:absolute}
  .brand{left:53px;top:66px;display:flex;align-items:center;gap:12px}
  .brand-square{width:40px;height:40px;background:var(--ink)}
  .brand-text{display:flex;flex-direction:column}
  .brand-name{font-weight:600;font-size:40px;letter-spacing:4px;color:var(--ink);line-height:1}
  .brand-tag{font-weight:600;font-size:11.5px;letter-spacing:4.4px;color:var(--ink);margin-top:6px}
  .title{right:53px;top:58px;font-family:"Barlow Semi Condensed",sans-serif;font-weight:700;font-size:46px;color:var(--ink);line-height:1;letter-spacing:.3px}
  .subtitle{right:55px;top:104px;font-family:"Barlow Semi Condensed",sans-serif;font-weight:600;font-size:25px;color:var(--accent);line-height:1;letter-spacing:.2px}
  .rule{background:var(--rule);height:1px}
  .plan{left:53px;top:216px;width:356px;height:296px;background:var(--plan);border:5px solid var(--wall)}
  .room-floor{left:298px;top:294px;width:100px;height:102px;background:var(--room);border:5px solid var(--wall);display:flex;align-items:center;justify-content:center;text-align:center;font-weight:600;font-size:10.5px;line-height:1.2;color:var(--ink)}
  .dim-label{font-size:9px;color:var(--ink-dark)}
  .dim-label b{font-weight:700}
  .step{width:78px;height:78px;border-radius:50%;color:#fff;text-align:center;display:flex;flex-direction:column;justify-content:center;align-items:center}
  .step .lbl{font-size:17px;font-weight:400;line-height:1}
  .step .num{font-size:27px;font-weight:500;line-height:1}
  .step-one{left:561px;top:172px;background:var(--ink)}
  .step-two{left:562px;top:320px;background:var(--accent)}
  .center{left:456px;width:290px;text-align:center}
  .step-head{font-weight:700;font-size:9px;color:var(--ink-dark);letter-spacing:.1px}
  .formula{font-size:11px;color:var(--ink)}
  .formula b{font-weight:700}
  .formula.accent{color:var(--accent);font-weight:500}
  .note{font-size:8.8px;line-height:1.3}
  .note b{font-weight:700}
  .legend-note{font-size:7.4px;line-height:1.35}
  .legend-note .accent{color:var(--accent);font-weight:700;font-size:8.4px}
  .photo{left:934px;width:213px;height:109px}
  .colour-note{right:289px;top:368px;text-align:right;font-size:10px;color:var(--ink);line-height:1.3}
  .box-label{font-weight:700;font-size:8.5px;color:var(--ink);line-height:1.35}
  .big-sym{font-weight:700;color:var(--ink);font-size:30px;line-height:1}
  .contact{left:585px;top:567px}
  .contact-head{font-weight:700;font-size:8.8px;color:var(--ink)}
  .contact-row{display:flex;align-items:center;gap:6px;font-size:8.8px;color:var(--ink);margin-top:4px}
</style>
</head>
<body>

<div class="abs brand">
  <div class="brand-square"></div>
  <div class="brand-text">
    <span class="brand-name">VERANO</span>
    <span class="brand-tag">PREMIUM FLOORS AND TILES</span>
  </div>
</div>

<h1 class="abs title">SELF ADHESIVE VINYL PLANKS</h1>
<h2 class="abs subtitle">GUIDE TO MEASURING REQUIRED FLOOR PACKS ESTIMATION</h2>
<div class="abs rule" style="left:53px;top:137px;width:1094px"></div>

<div class="abs plan" role="img" aria-label="House floor plan with several rooms, doors and windows"></div>
<div class="abs room-floor">ROOM<br>FLOOR</div>

<svg class="abs" style="left:0;top:0" width="1200" height="675" aria-hidden="true">
  <defs>
    <marker id="arrowHead" markerWidth="6" markerHeight="6" refX="5" refY="3" orient="auto">
      <path d="M0,0 L6,3 L0,6 Z" fill="#5a5046"/>
    </marker>
  </defs>
  <g stroke="#8a8178" stroke-width=".7" fill="none">
    <line x1="300" y1="247" x2="394" y2="247"/>
    <line x1="301" y1="241" x2="301" y2="253"/>
    <line x1="393" y1="241" x2="393" y2="288"/>
    <line x1="430" y1="297" x2="430" y2="391"/>
    <line x1="420" y1="298" x2="440" y2="298"/>
    <line x1="420" y1="390" x2="440" y2="390"/>
  </g>
  <g stroke="#5a5046" stroke-width=".8" stroke-dasharray="1.5 2" fill="none">
    <path d="M349,222 L349,212 Q349,208 353,208 L552,208" marker-end="url(#arrowHead)"/>
    <path d="M450,327 L450,270 Q450,220 500,220 L552,220" marker-end="url(#arrowHead)"/>
  </g>
  <g fill="#fff" stroke="#5a5046" stroke-width=".8">
    <circle cx="349" cy="225" r="2.5"/>
    <circle cx="450" cy="330" r="2.5"/>
  </g>
  <line x1="601" y1="296" x2="601" y2="308" stroke="#5a5046" stroke-width="1.4"/>
  <path d="M597,306 L601,313 L605,306 Z" fill="#5a5046"/>
  <rect x="652" y="340" width="9" height="4" fill="#9c6630"/>
  <rect x="652" y="351" width="9" height="4" fill="#e0e0e0"/>
  <rect x="652" y="362" width="9" height="4" fill="#e5b26f"/>
  <rect x="652" y="373" width="9" height="4" fill="#7c7772"/>
  <g fill="none" stroke-width=".8" stroke-dasharray="1.2 1.6">
    <path d="M663,342 C760,330 770,200 883,194" stroke="#b57233"/>
    <path d="M663,353 C760,340 780,318 883,318" stroke="#d4d4d4"/>
    <path d="M663,364 C760,362 780,442 883,442" stroke="#e5b26f"/>
    <path d="M663,375 C760,380 760,567 883,567" stroke="#6e6860"/>
  </g>
  <g fill="#fff" stroke-width=".8">
    <circle cx="885" cy="194" r="2.5" stroke="#b57233"/>
    <circle cx="885" cy="318" r="2.5" stroke="#d4d4d4"/>
    <circle cx="885" cy="442" r="2.5" stroke="#e5b26f"/>
    <circle cx="885" cy="567" r="2.5" stroke="#6e6860"/>
  </g>
  <circle cx="904" cy="194" r="7" fill="#5b3f2e"/>
  <circle cx="904" cy="318" r="7" fill="#e2e2e2"/>
  <circle cx="904" cy="442" r="7" fill="#e5b26f"/>
  <circle cx="904" cy="567" r="7" fill="#a9a49c"/>
  <line x1="456" y1="473" x2="745" y2="473" stroke="#5a5046" stroke-width=".8"/>
  <line x1="53" y1="553" x2="745" y2="553" stroke="#c9c2b8" stroke-width=".8"/>
  <line x1="53" y1="622" x2="745" y2="622" stroke="#c9c2b8" stroke-width=".8"/>
  <line x1="570" y1="566" x2="570" y2="609" stroke="#5a5046" stroke-width="1.4"/>
  <g fill="none" stroke="#5a5046" stroke-width="1.6" stroke-linejoin="round">
    <path d="M62,574 L86,562 L110,574 L110,599 L86,611 L62,599 Z"/>
    <path d="M62,574 L86,586 L110,574 M86,586 L86,611"/>
    <path d="M74,568 L98,580 L98,588"/>
  </g>
  <g fill="#fff" stroke="#5a5046" stroke-width=".9" stroke-linejoin="round">
    <path d="M184,600 L219,613 L255,600 L219,587 Z"/>
    <path d="M184,596 L219,609 L255,596 L219,583 Z"/>
    <path d="M184,592 L219,605 L255,592 L219,579 Z"/>
    <path d="M184,588 L219,601 L255,588 L219,575 Z"/>
    <path d="M184,584 L219,597 L255,584 L219,571 Z"/>
    <path d="M184,580 L219,593 L255,580 L219,567 Z"/>
    <path d="M184,576 L219,589 L255,576 L219,563 Z"/>
  </g>
  <path d="M353,587 L399,561 L445,587 L399,613 Z" fill="none" stroke="#5a5046" stroke-width="1"/>
</svg>

<div class="abs dim-label" style="left:330px;top:232px"><b>L</b> meters</div>
<div class="abs dim-label" style="left:436px;top:338px"><b>W</b> meters</div>

<div class="abs step step-one"><span class="lbl">STEP</span><span class="num">1</span></div>
<div class="abs center step-head" style="top:256px">MEASURE ROOM DIMENSIONS</div>
<div class="abs center formula" style="top:269px">Floor Total Area: <b>L X W = T</b></div>

<div class="abs step step-two"><span class="lbl">STEP</span><span class="num">2</span></div>
<div class="abs center step-head" style="top:404px">COMPUTE FLOOR PACKS REQUIRED</div>
<div class="abs center formula accent" style="top:418px">Packs: Total Area (T) / 5 = B</div>
<div class="abs center note" style="top:437px"><b>NB:</b> One box of planks covers<br>a total area of 5m²</div>

<div class="abs center legend-note" style="left:446px;width:310px;top:489px">
  <span class="accent">B = Total number of boxes required for the total measured area</span><br>
  (always round off the figure to the nearest tenth when in decimal points)
</div>
<div class="abs center legend-note" style="left:446px;width:310px;top:515px">
  (If your room is not a regular rectangle / square, share a simple drawing sketch<br>
  and send it to us, we will be able to work out the total area for you).
</div>

<div class="abs box-label" style="left:118px;top:581px">1 BOX</div>
<div class="abs big-sym" style="left:153px;top:571px">=</div>
<div class="abs box-label" style="left:264px;top:570px">36 PCS<br>FLOOR<br>PLANKS</div>
<div class="abs big-sym" style="left:316px;top:571px">&gt;</div>
<div class="abs" style="left:383px;top:577px;font-weight:700;font-size:16px;color:var(--ink)">5m<sup style="font-size:9px">2</sup></div>
<div class="abs box-label" style="left:457px;top:576px">TOTAL AREA<br>COVERAGE</div>

<div class="abs contact">
  <div class="contact-head">FOR MORE INFORMATION CONTACT</div>
  <div class="contact-row">
    <svg width="11" height="11" viewBox="0 0 24 24" fill="none" stroke="#5a5046" stroke-width="2"><path d="M5 3h4l2 5-3 2a11 11 0 0 0 6 6l2-3 5 2v4a2 2 0 0 1-2 2A17 17 0 0 1 3 5a2 2 0 0 1 2-2z"/></svg>
    <span>+44 000 000 000</span>
  </div>
  <div class="contact-row">
    <svg width="12" height="10" viewBox="0 0 24 18" fill="none" stroke="#5a5046" stroke-width="2"><rect x="1" y="1" width="22" height="16"/><path d="M1 1l11 9 11-9"/></svg>
    <span>info@veranofloors.co.uk</span>
  </div>
</div>

<div class="abs colour-note">Vinyl planks available in<br>different colour choices</div>

<div class="abs photo" style="top:150px;background:linear-gradient(180deg,#2e3a38 0%,#3f4a44 55%,#4a3428 70%,#3a281e 100%)" role="img" aria-label="Living room with a green sofa on dark brown vinyl planks"></div>
<div class="abs photo" style="top:271px;background:linear-gradient(180deg,#e6e6e4 0%,#d9d8d5 60%,#cfcdc9 100%)" role="img" aria-label="Wooden chair on light grey vinyl planks"></div>
<div class="abs photo" style="top:392px;background:linear-gradient(180deg,#ececea 0%,#d6d4d0 55%,#d9a666 70%,#c98f4e 100%)" role="img" aria-label="Hallway with white door on golden oak vinyl planks"></div>
<div class="abs photo" style="top:512px;background:linear-gradient(180deg,#eeeeee 0%,#d8d8d8 50%,#9e9a94 72%,#8d8983 100%)" role="img" aria-label="Bedroom with red blanket on grey vinyl planks"></div>

</body>
</html>
```